Business Card for Technology Startup

Design a 2-sided business card using the logo provided. We are a digital healthcare platform that provides a mobile app and web UI that helps caregivers, families, and doctors share information and provide better patient outcomes. We use AI and machine learning to help guide patients through their day-to-day life. The final design should communicate stability, peace, comfort, but also align with the image of an AI-driven technology startup.

I'd like the deliverable to by a Photoshop PSD file (with layers) that I can work with in pixlr.com. Should contain the following editable layers:
Name (ex. John Doe)
Title (ex. Founder / CEO)
Email (ex. info@brenvaxa.ai)
Phone (ex. (555) 214-7780)
Website (ex. https://brenvaxa.ai)

```html
<!DOCTYPE html>
<html lang="en">
<head>
<meta charset="utf-8">
<title>Brenvaxa Business Card</title>
<link rel="stylesheet" href="https://fonts.googleapis.com/css2?family=Poppins:wght@400;600;700&family=Lato:wght@400&display=swap">
<style>
  :root {
    --page-bg: #e6e8ea;
    --card-white: #ffffff;
    --card-grey: #ececec;
    --brand-blue: #1fa9dc;
    --soft-blue: #d6e8ef;
    --ink: #111111;
    --muted-ink: #333333;
    --rule: #8a8a8a;
    --frame-dark: #0b0b0b;
  }
  * { box-sizing: border-box; margin: 0; padding: 0; }
  html, body {
    width: 1200px;
    height: 900px;
    overflow: hidden;
    background: var(--page-bg);
  }
  .canvas {
    position: relative;
    width: 1200px;
    height: 900px;
  }
  .card {
    position: absolute;
    left: 285px;
    width: 630px;
    height: 360px;
    padding: 10px;
    box-shadow: 0 10px 30px rgba(0,0,0,0.18);
  }
  .card--front { top: 70px; background: var(--brand-blue); }
  .card--back { top: 480px; background: var(--frame-dark); }
  .card__face {
    position: relative;
    width: 100%;
    height: 100%;
    overflow: hidden;
    background: linear-gradient(115deg, var(--card-grey) 0%, var(--card-white) 70%);
  }
  .card__glow {
    position: absolute;
    width: 260px;
    height: 260px;
    border-radius: 50%;
    background: var(--soft-blue);
    opacity: 0.7;
  }
  .card--front .card__glow { left: 190px; top: 60px; }
  .card--back .card__glow { left: 200px; top: 30px; }
  .wordmark {
    position: relative;
    display: flex;
    align-items: center;
    gap: 14px;
  }
  .wordmark__dot {
    width: 22px;
    height: 22px;
    border-radius: 50%;
    background: var(--brand-blue);
  }
  .wordmark__name {
    font-family: "Poppins", sans-serif;
    font-weight: 700;
    color: var(--ink);
    letter-spacing: 0.5px;
    line-height: 1;
  }
  .card--front .card__face {
    display: flex;
    align-items: center;
    justify-content: center;
  }
  .card--front .wordmark__name { font-size: 58px; }
  .card--back .card__face {
    display: flex;
    flex-direction: column;
    align-items: center;
    padding-top: 52px;
  }
  .card--back .wordmark__name { font-size: 50px; }
  .identity {
    position: relative;
    margin-top: 26px;
    font-family: "Poppins", sans-serif;
    font-size: 19px;
    color: var(--ink);
  }
  .identity__name { font-weight: 700; letter-spacing: 0.5px; }
  .identity__sep { font-weight: 600; margin: 0 6px; }
  .identity__title { font-weight: 400; color: var(--brand-blue); }
  .contact {
    position: relative;
    display: flex;
    align-items: center;
    gap: 8px;
    font-family: "Lato", sans-serif;
    font-size: 16px;
    color: var(--muted-ink);
  }
  .contact--phone { margin-top: 14px; }
  .divider {
    position: relative;
    width: 380px;
    height: 1px;
    background: var(--rule);
    margin: 16px 0;
  }
  .contact-row {
    position: relative;
    display: flex;
    align-items: center;
    gap: 10px;
  }
  .contact-row__bar {
    font-family: "Lato", sans-serif;
    color: var(--muted-ink);
  }
  .icon { width: 16px; height: 16px; flex: none; }
</style>
</head>
<body>
<main class="canvas">

  <section class="card card--front" aria-label="Business card front">
    <div class="card__face">
      <div class="card__glow"></div>
      <div class="wordmark">
        <span class="wordmark__dot"></span>
        <span class="wordmark__name">brenvaxa</span>
      </div>
    </div>
  </section>

  <section class="card card--back" aria-label="Business card back">
    <div class="card__face">
      <div class="card__glow"></div>
      <div class="wordmark">
        <span class="wordmark__dot"></span>
        <span class="wordmark__name">brenvaxa</span>
      </div>

      <p class="identity">
        <span class="identity__name">JOHN DOE</span><span class="identity__sep">|</span><span class="identity__title">Founder / CEO</span>
      </p>

      <p class="contact contact--phone">
        <svg class="icon" viewBox="0 0 24 24" aria-hidden="true">
          <path fill="#1fa9dc" d="M6.6 10.8a15.1 15.1 0 0 0 6.6 6.6l2.2-2.2a1 1 0 0 1 1-.25 11.4 11.4 0 0 0 3.6.57 1 1 0 0 1 1 1V20a1 1 0 0 1-1 1A17 17 0 0 1 3 4a1 1 0 0 1 1-1h3.5a1 1 0 0 1 1 1c0 1.25.2 2.45.57 3.6a1 1 0 0 1-.25 1z"/>
        </svg>
        (555) 214-7780
      </p>

      <div class="divider"></div>

      <div class="contact-row">
        <p class="contact">
          <svg class="icon" viewBox="0 0 24 24" aria-hidden="true">
            <rect x="2" y="5" width="20" height="14" rx="1.5" fill="#1fa9dc"/>
            <path d="M3 6l9 7 9-7" fill="none" stroke="#ffffff" stroke-width="1.6"/>
          </svg>
          info@brenvaxa.ai
        </p>
        <span class="contact-row__bar">|</span>
        <p class="contact">
          <svg class="icon" viewBox="0 0 24 24" aria-hidden="true">
            <g fill="none" stroke="#1fa9dc" stroke-width="1.6">
              <circle cx="12" cy="12" r="9"/>
              <ellipse cx="12" cy="12" rx="4" ry="9"/>
              <path d="M3 12h18M5 7.5h14M5 16.5h14"/>
            </g>
          </svg>
          www.brenvaxa.ai
        </p>
      </div>
    </div>
  </section>

</main>
</body>
</html>
```